Fundvane Informational Banners for Ashen Tide Rising

Hello, We are currently in the Process of doing a Fundvane Campaign which is due on the 4th. We need a Grungy/Dirty Dark Dead Feeling set of Banners, and Informational Pieces in Various Sizes.
Banner Sizes:
640px × 88px Normall Banner
640px × 57px Breaker Banner
700px × 93px Header Banner
640px × 635px Display Box for Rewards
A Larger box, that needs to have a Seamless beginning and ending also needs to be made, so it can be extended as more text and so-forth is completed.

We are looking for very Dead, Dark looking images, thesr are ment to be displayed on the fundvane webpage they need to flow well with the fundvane form, as well as show off our things, simple or advanced. They need to match our style.

NOTE IMPORTANT!!!!
THESE ARE NOT ADVERTISING BANNERS, THESE ARE BANNERS FOR THE FUNDVANE WEBSITE FOR A CAMPAIGN PLEASE DO SOME HOMEWORK BEFORE ATTEMPTING THESE IMAGES WE ARE NOT LOOKING FOR ADVERTISING BANNERS WE ARE LOOKING FOR INFORMATIONAL PIECES

Example of words that will be used on the various Banners

"Physical Add-ons"
"Digital Add-ons"
"Who we are"
"What is Ashen Tide Rising?"
"What is Procedural Generation?"
"Why are you Attempting this?"

THESE ARE EXAMPLE SENTENCES THAT WILL BE IN THE BANNERS I REPEAT THESE ARE NOT ADVERTISING WEBBANNERS
Updates

Everyone is Doing wonderful, thank you all for making such lovely work. thank You. Keep it up, remember undead feel, it must be functional piece on the fundvane website. :3 

Target Market(s)

Zombie, and Undead ages People 13-51 that are Gamers

Industry/Entity Type

Digital

Requirements
Must have
• These Designs must be Boxes and Banners, and Break Points for a Fundvane Information Display I will provide a few links here.
http://www.fundvane-example.com/projects/brevmoor/harrow-veils-of-quillan
http://www.fundvane-example.com/projects/corvale/venture-paragon

Our Artwork Style & Concept Artwork can be found here
http://www.gamevault-example.net/games/ashen-tide-rising/images

```html
<!DOCTYPE html>
<html lang="en">
<head>
<meta charset="utf-8">
<title>What is Ashen Tide Rising? — Section Banner</title>
<link rel="stylesheet" href="https://fonts.googleapis.com/css2?family=Cinzel:wght@600;700&display=swap">
<style>
  :root {
    --ink-black: #0a0a08;
    --moss-dark: #1f2619;
    --moss-mid: #3a4530;
    --blood-red: #6e1f1c;
    --rust-red: #8a2e26;
    --ash-grey: #4a4f52;
    --gold-light: #fff1b8;
    --gold-mid: #e2b85a;
    --gold-deep: #9c6a1e;
    --text-edge: #1a0f05;
  }
  html, body {
    margin: 0;
    padding: 0;
    width: 1200px;
    height: 165px;
    overflow: hidden;
    background: var(--ink-black);
  }
  .section-banner {
    position: relative;
    width: 1200px;
    height: 165px;
    overflow: hidden;
  }
  .banner-backdrop {
    position: absolute;
    inset: 0;
    background:
      radial-gradient(ellipse 420px 200px at 0% 10%, var(--rust-red) 0%, transparent 70%),
      radial-gradient(ellipse 380px 200px at 100% 100%, var(--blood-red) 0%, transparent 70%),
      radial-gradient(ellipse 300px 120px at 100% 0%, var(--blood-red) 0%, transparent 75%),
      radial-gradient(ellipse 500px 110px at 50% 45%, var(--ash-grey) 0%, transparent 70%),
      linear-gradient(180deg, var(--moss-mid) 0%, var(--moss-dark) 45%, var(--ink-black) 100%);
  }
  .banner-vignette {
    position: absolute;
    inset: 0;
    box-shadow: inset 0 0 60px 20px rgba(0,0,0,0.75);
  }
  .banner-title {
    position: absolute;
    inset: 0;
    width: 1200px;
    height: 165px;
  }
  .banner-title text {
    font-family: "Cinzel", "Trajan Pro", serif;
    font-weight: 700;
    font-size: 84px;
    font-variant: small-caps;
  }
</style>
</head>
<body>
  <header class="section-banner">
    <div class="banner-backdrop" role="img" aria-label="Dark grungy undead scenery in murky green and black with blood-red smears in the corners"></div>
    <div class="banner-vignette"></div>
    <svg class="banner-title" viewBox="0 0 1200 165" aria-labelledby="banner-heading">
      <defs>
        <linearGradient id="gold-fill" x1="0" y1="0" x2="0" y2="1">
          <stop offset="0" stop-color="var(--gold-light)"/>
          <stop offset="0.45" stop-color="var(--gold-mid)"/>
          <stop offset="1" stop-color="var(--gold-deep)"/>
        </linearGradient>
        <filter id="title-shadow" x="-5%" y="-30%" width="110%" height="160%">
          <feDropShadow dx="2" dy="3" stdDeviation="3" flood-color="#000" flood-opacity="0.9"/>
        </filter>
      </defs>
      <text id="banner-heading" x="600" y="114" text-anchor="middle"
            textLength="1150" lengthAdjust="spacingAndGlyphs"
            fill="url(#gold-fill)" stroke="var(--text-edge)" stroke-width="2"
            paint-order="stroke" filter="url(#title-shadow)">What is Ashen Tide Rising?</text>
    </svg>
  </header>
</body>
</html>
```